Business Cards for a law firm

Business cards for our law firm. Use our silhoette logo and OAK HARBOR - check our website (www.oakharbor-legal.com)

Contact Information for Business Card

our silhouette logo, OAK HARBOR, 800-555-0147, Dorian Kestrup, dorian@oakharbor-legal.com

Requirements
Must have
• our silhouette logo, OAK HARBOR, 800-555-0147, Dorian Kestrup, dorian@oakharbor-legal.com

```html
<!DOCTYPE html>
<html lang="en">
<head>
<meta charset="utf-8">
<title>Oak Harbor Injury Attorneys – Business Cards</title>
<link rel="stylesheet" href="https://fonts.googleapis.com/css2?family=Fira+Sans:wght@500;600;700&display=swap">
<style>
  :root {
    --navy: #023f7e;
    --teal: #0892ba;
    --teal-text: #0785ad;
    --white: #ffffff;
    --page: #ffffff;
    --shadow: rgba(0, 0, 0, 0.22);
    --gradient: linear-gradient(70deg, var(--navy) 15%, var(--teal) 100%);
  }
  * { margin: 0; padding: 0; box-sizing: border-box; }
  html, body {
    width: 1100px; height: 1200px; overflow: hidden;
    background: var(--page);
    font-family: "Fira Sans", Arial, sans-serif;
  }
  .canvas { position: relative; width: 1100px; height: 1200px; }

  .card {
    position: absolute; left: 116px; width: 876px; height: 478px;
    background: var(--white);
    box-shadow: 0 14px 28px var(--shadow);
  }
  .card--front { top: 63px; }
  .card--back { top: 668px; overflow: hidden; }

  /* Front */
  .front-panel {
    position: absolute; left: 24px; top: 13px; width: 828px; height: 453px;
    background: var(--gradient);
    display: flex; align-items: center; justify-content: center;
  }
  .brand { display: flex; align-items: center; gap: 22px; color: var(--white); }
  .brand-mark { width: 64px; height: 64px; background: var(--white); }
  .brand-text { text-align: center; }
  .brand-name { font-weight: 600; font-size: 56px; letter-spacing: 4px; line-height: 1; }
  .brand-tagline { font-weight: 600; font-size: 24px; letter-spacing: 9px; margin-top: 12px; }

  /* Back */
  .back-brand { position: absolute; left: 71px; top: 56px; color: var(--navy); gap: 16px; }
  .back-brand .brand-mark { width: 52px; height: 52px; background: var(--navy); }
  .back-brand .brand-name { font-size: 38px; letter-spacing: 3px; color: var(--navy); }
  .back-brand .brand-tagline { font-size: 17px; letter-spacing: 6px; margin-top: 8px; color: var(--teal-text); }

  .name-band {
    position: absolute; left: 24px; top: 178px; width: 828px; height: 100px;
    background: linear-gradient(90deg, var(--navy) 0%, var(--teal) 100%);
    color: var(--white);
    padding: 20px 0 0 47px;
  }
  .name-label { font-weight: 600; font-size: 29px; letter-spacing: 5px; line-height: 1; }
  .name-list { font-weight: 700; font-size: 16px; letter-spacing: 1.5px; margin-top: 20px; display: flex; gap: 18px; }

  .portrait {
    position: absolute; left: 541px; top: 103px; width: 250px; height: 250px;
    border-radius: 50%;
    border: 3px solid var(--teal);
    background: var(--white);
    padding: 4px;
  }
  .portrait-fill {
    width: 100%; height: 100%; border-radius: 50%;
    background: linear-gradient(180deg, #f4f4f4 0%, #e6dcd6 38%, #2b2f3d 62%, #1e2231 100%);
  }

  .contacts { position: absolute; left: 71px; top: 318px; list-style: none; color: var(--teal-text); font-weight: 600; }
  .contact { display: flex; align-items: center; gap: 10px; height: 24px; }
  .contact + .contact { margin-top: 24px; }
  .contact--phone { font-size: 25px; letter-spacing: 1.5px; }
  .contact--email { font-size: 24px; letter-spacing: 1.2px; }
  .contact--web { font-size: 20px; letter-spacing: 1px; }
  .contact-icon { width: 18px; height: 18px; flex: none; }
</style>
</head>
<body>
<div class="canvas">

  <section class="card card--front" aria-label="Card front">
    <div class="front-panel">
      <div class="brand">
        <span class="brand-mark" aria-hidden="true"></span>
        <div class="brand-text">
          <div class="brand-name">OAK HARBOR</div>
          <div class="brand-tagline">INJURY ATTORNEYS</div>
        </div>
      </div>
    </div>
  </section>

  <section class="card card--back" aria-label="Card back">
    <div class="brand back-brand">
      <span class="brand-mark" aria-hidden="true"></span>
      <div class="brand-text">
        <div class="brand-name">OAK HARBOR</div>
        <div class="brand-tagline">INJURY ATTORNEYS</div>
      </div>
    </div>

    <div class="name-band">
      <div class="name-label">LAWYER NAME:</div>
      <div class="name-list"><span>DORIAN KESTRUP</span><span>MARCUS KESTRUP</span></div>
    </div>

    <div class="portrait">
      <div class="portrait-fill" role="img" aria-label="Portrait photo of the two attorneys in dark suits"></div>
    </div>

    <ul class="contacts">
      <li class="contact contact--phone">
        <svg class="contact-icon" viewBox="0 0 20 20" aria-hidden="true">
          <circle cx="10" cy="10" r="10" fill="#023f7e"/>
          <path d="M6.5 5.2c.5-.4 1.1-.3 1.4.2l.9 1.5c.2.4.1.9-.2 1.2l-.6.5c.5 1.2 1.4 2.1 2.6 2.6l.5-.6c.3-.3.8-.4 1.2-.2l1.5.9c.5.3.6.9.2 1.4l-.7.8c-.5.5-1.3.6-2 .3-2.4-1-4.3-2.9-5.3-5.3-.3-.7-.2-1.5.3-2z" fill="#fff"/>
        </svg>
        800-555-0147
      </li>
      <li class="contact contact--email">
        <svg class="contact-icon" viewBox="0 0 20 20" aria-hidden="true">
          <circle cx="10" cy="10" r="10" fill="#023f7e"/>
          <rect x="5" y="6.5" width="10" height="7" rx="1" fill="none" stroke="#fff" stroke-width="1.2"/>
          <path d="M5.3 7l4.7 3.6L14.7 7" fill="none" stroke="#fff" stroke-width="1.2"/>
        </svg>
        DORIAN@OAKHARBOR-LEGAL.COM
      </li>
      <li class="contact contact--web">
        <svg class="contact-icon" viewBox="0 0 20 20" aria-hidden="true">
          <circle cx="10" cy="10" r="10" fill="#023f7e"/>
          <g fill="none" stroke="#fff" stroke-width="1">
            <circle cx="10" cy="10" r="5.5"/>
            <ellipse cx="10" cy="10" rx="2.4" ry="5.5"/>
            <path d="M4.5 10h11M5.3 7.2h9.4M5.3 12.8h9.4"/>
          </g>
        </svg>
        WWW.OAKHARBOR-LEGAL.COM
      </li>
    </ul>
  </section>

</div>
</body>
</html>
```